Velqor5 Business Card - Health

Velqor5 maximizes value from the health data of its clients, including doctors, HMOs, and patients. I have attached the Velqor5 logo as an ai and eps file.
Target Market(s)
Health, HMO, Healthcare, Data, Big Data, Data Analytics
Industry/Entity Type
Business
Requirements
Must have
- At least one side should have some white on it so that we can write on it.

```html
<!DOCTYPE html>
<html lang="en">
<head>
<meta charset="utf-8">
<title>Velqor5 Business Card</title>
<link rel="stylesheet" href="https://fonts.googleapis.com/css2?family=Jost:wght@400;500&display=swap">
<style>
  :root {
    --page-bg: #e4e6ea;
    --card-bg: #ffffff;
    --brand-blue: #2f6fd6;
    --panel-deep: #1d3fa8;
    --panel-mid: #2b5fd0;
    --panel-light: #3f7fe6;
    --name-blue: #2a6fb5;
    --ink: #1e1f24;
    --panel-text: #e2eaf7;
  }
  * { margin: 0; padding: 0; box-sizing: border-box; }
  html, body {
    width: 1200px;
    height: 969px;
    overflow: hidden;
    background: var(--page-bg);
    font-family: "Jost", sans-serif;
  }
  .card {
    position: absolute;
    left: 100px;
    top: 199px;
    width: 1000px;
    height: 571px;
    background: var(--card-bg);
    overflow: hidden;
    box-shadow: 0 10px 30px rgba(0, 0, 0, 0.12);
  }
  .contact-panel {
    position: absolute;
    left: 0;
    top: 0;
    width: 1000px;
    height: 571px;
  }
  .brand {
    position: absolute;
    left: 46px;
    top: 72px;
    display: flex;
    align-items: center;
    gap: 32px;
  }
  .brand-dot {
    width: 128px;
    height: 128px;
    border-radius: 50%;
    background: var(--brand-blue);
  }
  .brand-name {
    font-size: 92px;
    font-weight: 400;
    color: var(--ink);
    letter-spacing: -1px;
    line-height: 1;
  }
  .address {
    position: absolute;
    right: 62px;
    top: 272px;
    text-align: right;
    color: var(--panel-text);
    font-size: 24px;
    line-height: 32px;
  }
  .contact-list {
    position: absolute;
    right: 20px;
    top: 352px;
    list-style: none;
  }
  .contact-list li {
    display: flex;
    justify-content: flex-end;
    align-items: center;
    gap: 14px;
    height: 38px;
    color: var(--panel-text);
    font-size: 23px;
  }
  .contact-list svg {
    width: 26px;
    height: 26px;
    flex: none;
    fill: none;
    stroke: var(--panel-text);
    stroke-width: 2;
    stroke-linecap: round;
    stroke-linejoin: round;
  }
  .person {
    position: absolute;
    left: 55px;
    top: 452px;
  }
  .person-name {
    font-size: 36px;
    font-weight: 400;
    color: var(--name-blue);
    line-height: 44px;
  }
  .person-title {
    font-size: 27px;
    color: var(--ink);
    line-height: 36px;
  }
</style>
</head>
<body>
  <div class="card">
    <svg class="contact-panel" viewBox="0 0 1000 571" aria-hidden="true">
      <defs>
        <linearGradient id="panelFill" x1="0" y1="0" x2="1" y2="1">
          <stop offset="0" stop-color="var(--panel-light)"/>
          <stop offset="0.45" stop-color="var(--panel-mid)"/>
          <stop offset="1" stop-color="var(--panel-deep)"/>
        </linearGradient>
      </defs>
      <polygon points="555,268 819,158 1000,250 1000,571 491,571" fill="url(#panelFill)"/>
      <polygon points="555,268 819,158 700,571 491,571" fill="#ffffff" opacity="0.06"/>
    </svg>

    <div class="brand">
      <div class="brand-dot"></div>
      <div class="brand-name">Velqor5</div>
    </div>

    <p class="address">4120 Larkspur Court<br>Tallmoor, Oregon 97562</p>
    <ul class="contact-list">
      <li>503 218 4470
        <svg viewBox="0 0 24 24"><path d="M5 3h4l2 5-2.5 1.5a11 11 0 0 0 6 6L16 13l5 2v4a2 2 0 0 1-2 2A17 17 0 0 1 3 5a2 2 0 0 1 2-2z"/></svg>
      </li>
      <li>503 719 2285
        <svg viewBox="0 0 24 24"><rect x="7" y="2" width="10" height="20" rx="2"/><line x1="11" y1="18" x2="13" y2="18"/></svg>
      </li>
      <li>503 218 4471
        <svg viewBox="0 0 24 24"><rect x="7" y="3" width="10" height="6"/><rect x="3" y="9" width="18" height="9" rx="1"/><rect x="7" y="15" width="10" height="6"/></svg>
      </li>
      <li>hello@velqor5.net
        <svg viewBox="0 0 24 24"><rect x="3" y="5" width="18" height="14" rx="1"/><path d="M3 6l9 7 9-7"/></svg>
      </li>
      <li>www.velqor5.net
        <svg viewBox="0 0 24 24"><circle cx="12" cy="12" r="9"/><ellipse cx="12" cy="12" rx="4" ry="9"/><line x1="3" y1="12" x2="21" y2="12"/></svg>
      </li>
    </ul>

    <div class="person">
      <p class="person-name">Marin Holt</p>
      <p class="person-title">CEO/Founder</p>
    </div>
  </div>
</body>
</html>
```